QV - menu design

Hi,

We require elegant menu design for upscale restaurant. Please find attached the logo and the menu items for your reference.

for inspiration, this is a good website: -
http://www.platewhisper.example/bellfoldnotes/about.php

We are very much open for Menu Size suggestions.

unfortunately the place is going under renovation, we don't have updated images to it. the closest look and feel to our place is http://varnelo.example ..

we are also open for creative options on the shape, the styles, etc. as long as it represents the fine dine feel ...

Thanks ...

Dear All,

We wouldlike to extend our apology for not being able to provide feedbacks on everysingle design. We were extremely busy and we have multiple contests opensimultaneously which makes the process even harder.

However,we would like to thank you all for the efforts you have put into designingour menu. It is very much appreciated …

We wishyou all success in your design ventures and we are quite positive that we willbe working with many of you on many projects in the soon future. 

Thanks & Regards,

TLG Team...

 

 

 

Industry/Entity Type

Restaurant

Requirements
Must have
• Please ensure that there are 'some' images in the menu ... this is very important.
Should not have
• IMPORTANT: -

1. Please DO NOT insert any currency sign to the menu
2. Please keep the prices of the menu at the end of the menu items descriptions NOT beside the menu item names. The font of the price should be similar to the menu item description and please DO NOT bold the numbers. the prices should be subtle.

Thank you ...

```html
<!DOCTYPE html>
<html lang="en">
<head>
<meta charset="utf-8">
<title>QV – Menu</title>
<link href="https://fonts.googleapis.com/css2?family=Ubuntu:wght@300;400;500;700&display=swap" rel="stylesheet">
<style>
:root{
  --page:#ffffff;
  --mocha:#987862;
  --mocha-deep:#8a6a54;
  --cream:#f3f1ef;
  --white:#ffffff;
  --dash:rgba(255,255,255,.55);
  --dash-dark:rgba(152,120,98,.6);
}
*{margin:0;padding:0;box-sizing:border-box}
html,body{width:1200px;height:609px;overflow:hidden;background:var(--page)}
body{font-family:"Ubuntu",sans-serif;position:relative}
.menu{position:absolute;left:55px;top:59px;width:1090px;height:490px;display:flex}
.panel{position:relative;width:218px;height:490px;overflow:hidden}
.panel--mocha{background:var(--mocha);color:var(--white)}
.panel--cream{background:var(--cream);color:var(--mocha-deep)}
.guides{position:absolute;inset:0;width:100%;height:100%}
.badge{position:absolute;border-radius:50%;display:flex;flex-direction:column;align-items:center;justify-content:center;text-align:center;line-height:1}
.badge--mocha{background:var(--mocha);color:var(--white)}
.badge--white{background:var(--white);color:var(--mocha)}
.badge small{font-size:9px;font-weight:300;letter-spacing:.5px}
.badge strong{font-size:11px;font-weight:500}
.cover-mark{left:10px;top:89px;width:196px;height:196px;color:var(--mocha)}
.cover-mark .brand{font-size:24px;font-weight:300;letter-spacing:5px;text-transform:uppercase}
.cover-mark .brand + .brand{font-size:11px;letter-spacing:4px;margin-top:8px}
.cover-label{left:68px;top:379px;width:80px;height:80px;font-size:18px;font-weight:300;color:var(--mocha)}
.items{position:absolute;left:17px;right:12px}
.item{margin-bottom:12px}
.item h3{font-size:9.5px;font-weight:700;letter-spacing:2.2px;line-height:1.05}
.item p{font-size:7.4px;font-weight:400;line-height:1.32}
.plain p{font-size:8.8px;font-weight:300;line-height:1.22;margin-bottom:9px}
.salad-list .item{margin-bottom:7px}
.salad-list .item h3{letter-spacing:2px}
.salad-list .item p{font-size:7.2px;line-height:1.26}
.photo{position:absolute;border-radius:50%;border:3px solid var(--white)}
</style>
</head>
<body>
<div class="menu">

  <section class="panel panel--mocha cover">
    <svg class="guides" viewBox="0 0 218 490" aria-hidden="true">
      <g stroke="var(--dash)" stroke-width="1" stroke-dasharray="4 4">
        <line x1="56" y1="0" x2="56" y2="490"/><line x1="83" y1="0" x2="83" y2="490"/>
        <line x1="131" y1="0" x2="131" y2="490"/><line x1="158" y1="0" x2="158" y2="490"/>
      </g>
      <line x1="108" y1="285" x2="108" y2="380" stroke="var(--white)" stroke-width="1"/>
    </svg>
    <div class="badge badge--white cover-mark">
      <span class="brand">Quill Vale</span>
      <span class="brand">Café</span>
    </div>
    <div class="badge badge--white cover-label">Menu</div>
  </section>

  <section class="panel panel--cream breakfast">
    <svg class="guides" viewBox="0 0 218 490" aria-hidden="true">
      <line x1="49" y1="0" x2="49" y2="15" stroke="var(--dash-dark)" stroke-dasharray="3 3"/>
      <line x1="49" y1="462" x2="49" y2="490" stroke="var(--dash-dark)" stroke-dasharray="3 3"/>
      <circle cx="49" cy="472" r="3.5" fill="var(--mocha)"/>
    </svg>
    <div class="badge badge--mocha" style="left:15px;top:15px;width:68px;height:68px"><small>THE</small><strong>BREAKFAST</strong></div>
    <div class="items" style="top:91px">
      <div class="item"><h3>Butter Croissant</h3><p>Served plain with a selection of two jams, a vanilla custard cream, a chocolate Cream and butter curls). 36</p></div>
      <div class="item"><h3>Cheese Croissant</h3><p>Crumbly freshly baked with cheese filling. 29</p></div>
      <div class="item"><h3>Daily Fresh Eggs</h3><p>A choice of poached, scrambled, pan fried, omelet) all served with toasted<br>Bread, mushrooms, roasted tomatoes and chicken sausages. 59</p></div>
      <div class="item"><h3>Healthy Time</h3><p>One choice of hot beverage from our cafe served with fruit salad, natural<br>Yoghurt, whole wheat bread vegetable sandwiches and sugar free biscuits selection.49</p></div>
      <div class="item"><h3>Energy Time</h3><p>One choice of hot beverage from our cafe served with finger chocolate muffins,<br>Poached egg with toasted bread and crispy beef bacon, crepe roll with goat<br>Cheese and honey and finger chocolate cream with salted cookies. 59</p></div>
      <div class="item"><h3>Quill Vale Time</h3><p>One choice of hot beverage from our cafe served with our selection of scones, Smoked salmon and avocado sandwich, roasted sausages sandwich, grilled vegetables sandwich, selection of our best biscuits. 59</p></div>
      <div class="item"><h3>The Arabic Breakfast</h3><p>Choice of Zattar Manakish and Cheese Manakish, served with one choice of hot beverage from our cafe and fresh orange juice. 59</p></div>
    </div>
  </section>

  <section class="panel panel--mocha sandwiches">
    <svg class="guides" viewBox="0 0 218 490" aria-hidden="true">
      <g stroke="var(--dash)" stroke-dasharray="3 3">
        <line x1="52" y1="0" x2="52" y2="15"/><line x1="52" y1="475" x2="52" y2="490"/>
        <line x1="143" y1="455" x2="143" y2="490"/>
      </g>
    </svg>
    <div class="badge badge--white" style="left:14px;top:15px;width:76px;height:76px"><small>THE</small><strong>SANDWICHES</strong></div>
    <div class="items plain" style="top:106px;right:14px">
      <p>Grilled Vegetables Sandwich with fresh Goat cheese and chives served with our Homemade spicy garlic mayo. 59</p>
      <p>Butterfish burger with fresh tomato, beef bacon, grilled vegetables and béarnaise sauce.</p>
      <p>Tataki Tuna sandwich with red onion slices, stewed endives and black olives and sultanas pate'. 79</p>
      <p style="margin-bottom:0">Beef sirloin steak sandwich with grain mustard, Parmesan cheese and fresh<br>Nashi pears. 79</p>
      <p>The Traditional Club sandwich served with French fries and vegetable chips. 69</p>
      <p>Chicken sandwich with Parmesan cheese slices, sundried tomatoes and mint<br>Flavored mayo. 69</p>
    </div>
    <div class="photo" role="img" aria-label="Photo of a grilled vegetable sandwich" style="left:82px;top:334px;width:126px;height:126px;background:radial-gradient(circle at 45% 50%,#c8553d,#7a8a45 45%,#d9b98a 75%)"></div>
    <div class="photo" role="img" aria-label="Photo of a small sandwich half" style="left:14px;top:402px;width:72px;height:72px;background:radial-gradient(circle,#c45a45,#8e9c5a 55%,#e0cfa9)"></div>
  </section>

  <section class="panel panel--cream soup">
    <svg class="guides" viewBox="0 0 218 490" aria-hidden="true">
      <g stroke="var(--dash-dark)" stroke-dasharray="3 3">
        <line x1="49" y1="0" x2="49" y2="30"/><line x1="49" y1="405" x2="49" y2="490"/>
        <line x1="110" y1="340" x2="110" y2="490"/><line x1="168" y1="405" x2="168" y2="490"/>
      </g>
    </svg>
    <div class="badge badge--mocha" style="left:16px;top:31px;width:65px;height:65px"><strong>SOUP</strong></div>
    <div class="items" style="top:108px">
      <div class="item"><h3>Bouillabaisse</h3><p>Traditional French Seafood soup, with Saffron and Estragon. 119</p></div>
      <div class="item"><h3>Barley soup</h3><p>With fresh vegetables, tomato smoothie and a hint of garlic oil. 49</p></div>
      <div class="item"><h3>Beef chili</h3><p>Served with Arabic bread, fresh guacamole and spicy black beans. 49</p></div>
    </div>
    <div class="photo" role="img" aria-label="Photo of a seafood soup with mussels" style="left:57px;top:234px;width:106px;height:106px;background:radial-gradient(circle,#c0482f,#3a3530 55%,#e8e4e0)"></div>
    <div class="photo" role="img" aria-label="Photo of a barley vegetable soup" style="left:12px;top:327px;width:78px;height:78px;background:radial-gradient(circle,#d9a23b,#c77a3a 55%,#efe9e2)"></div>
    <div class="photo" role="img" aria-label="Photo of a bowl of beef chili" style="left:128px;top:327px;width:78px;height:78px;background:radial-gradient(circle,#a2432c,#7a2f20 60%,#e4dcd4)"></div>
  </section>

  <section class="panel panel--mocha salads">
    <svg class="guides" viewBox="0 0 218 490" aria-hidden="true">
      <g stroke="var(--dash)" stroke-dasharray="3 3">
        <line x1="47" y1="0" x2="47" y2="18"/><line x1="45" y1="440" x2="45" y2="490"/>
        <line x1="110" y1="460" x2="110" y2="490"/><line x1="173" y1="440" x2="173" y2="490"/>
      </g>
    </svg>
    <div class="badge badge--white" style="left:14px;top:18px;width:66px;height:66px"><strong>SALADS</strong></div>
    <div class="items salad-list" style="top:96px;right:8px">
      <div class="item"><h3>Vegetarian Salad</h3><p>Fresh green leaves, Italian cherry tomatoes, carrots, cucumber, green apple and toasted pine nuts with our special grain mustard dressing.59</p></div>
      <div class="item"><h3>Sweet Gorgonzola Cheese Salad</h3><p>Fresh green leaves, Gorgonzola cheese, fresh pears, walnuts, garlic bread croutons, green celery with smoked honey dressing.59</p></div>
      <div class="item"><h3>Beef Sirloin Salad</h3><p>Fresh green leaves, beef sirloin julienne, caramelized apples, Parmesan cheese, toasted almonds, sundried tomatoes and light Pesto sauce.79</p></div>
      <div class="item"><h3>Tandoori Chicken Salad</h3><p>Fresh green leaves, Tandoori chicken breast, fresh mango, fresh goat cheese, crispy chicken skin and Jasmine rice sauce.69</p></div>
      <div class="item"><h3>Sea food Salad</h3><p>Fresh green leaves, fresh steamed seafood, black olives, celery, garlic bread croutons, avocado and grapefruit dressing.89</p></div>
      <div class="item"><h3>Fresh Tuna Salad</h3><p>Fresh green leaves, low temperature cooked tuna, taggiasca olives, red onions, roasted peppers, soy marinated tofu and lemon dressing.89</p></div>
    </div>
    <div class="photo" role="img" aria-label="Photo of a mixed vegetable salad" style="left:12px;top:380px;width:66px;height:66px;background:radial-gradient(circle,#c9a04a,#7f9a4e 55%,#ece6dc)"></div>
    <div class="photo" role="img" aria-label="Photo of a salmon salad" style="left:76px;top:400px;width:66px;height:66px;background:radial-gradient(circle,#d0683f,#6f8f45 55%,#e9e3d9)"></div>
    <div class="photo" role="img" aria-label="Photo of a seafood salad" style="left:140px;top:380px;width:66px;height:66px;background:radial-gradient(circle,#9a8c6a,#6e7d4a 55%,#e6e0d6)"></div>
  </section>

</div>
</body>
</html>
```